Business card design needed

Brenlo First Aid Training is a training provider in the Canberra region. We provide both public and private course bookings.

I want my business card to be fun/interesting. I have attached my own logo, however whatever you think works best will work for me.

Please see my website for more inspiration at www.brenlo-example.com.au

I would like a double sided design, and round corners please.

Some really good designs so far, just not quite the right one yet. 
Please look at my website for inspiration. 
Www.brenlo-example.com.au

Industry/Entity Type

Training

Contact Information for Business Card

Brenlo First Aid Training, Tobin Marsh, 0498563027, tobinmarsh4@mailvex-example.com.au, www.brenlo-example.com.au

```html
<!DOCTYPE html>
<html lang="en">
<head>
<meta charset="utf-8">
<title>Brenlo First Aid Training – Business Card</title>
<link rel="stylesheet" href="https://fonts.googleapis.com/css2?family=Oswald:wght@500&family=Roboto+Condensed:wght@400&display=swap">
<style>
  :root {
    --page-bg: #e9e6e1;
    --card-white: #ffffff;
    --card-shade: #e4e4e4;
    --brand-red: #c1272d;
    --brand-blue: #2e3a9a;
    --ink: #3a3a3a;
    --rule: #9a9a9a;
  }
  * { box-sizing: border-box; margin: 0; padding: 0; }
  html, body {
    width: 1200px; height: 1024px; overflow: hidden;
    background: var(--page-bg);
  }
  .sheet {
    width: 1200px; height: 1024px;
    display: flex; flex-direction: column; align-items: center; justify-content: center;
    gap: 44px;
  }
  .card {
    width: 770px; height: 440px;
    border-radius: 22px;
    overflow: hidden;
    position: relative;
    background: radial-gradient(ellipse at 45% 40%, var(--card-white) 0%, var(--card-white) 45%, var(--card-shade) 100%);
    box-shadow: 0 10px 26px rgba(0,0,0,0.18);
    border-bottom: 10px solid var(--brand-red);
  }

  /* Front */
  .card-front { display: flex; align-items: center; justify-content: center; }
  .brand-lockup { display: flex; align-items: center; gap: 20px; }
  .brand-mark { width: 54px; height: 54px; background: var(--brand-blue); }
  .brand-name {
    font-family: "Oswald", sans-serif; font-weight: 500;
    font-size: 46px; color: var(--brand-red); letter-spacing: 0.5px;
  }

  /* Back */
  .card-back { display: flex; align-items: center; padding: 0 48px 0 56px; }
  .back-brand { width: 250px; display: flex; align-items: center; gap: 12px; }
  .back-brand .brand-mark { width: 30px; height: 30px; flex: none; }
  .back-brand .brand-name { font-size: 24px; line-height: 1.15; }
  .divider { width: 1px; height: 300px; background: var(--rule); margin: 0 40px 0 20px; }
  .contact { display: flex; flex-direction: column; gap: 16px; }
  .person-name {
    font-family: "Oswald", sans-serif; font-weight: 500;
    font-size: 40px; color: var(--brand-red); margin-bottom: 6px;
  }
  .contact-row {
    display: flex; align-items: center; gap: 14px;
    font-family: "Roboto Condensed", sans-serif; font-size: 21px; color: var(--ink);
  }
  .contact-row.phone { font-size: 28px; }
  .contact-icon { width: 22px; height: 22px; flex: none; }
</style>
</head>
<body>
<main class="sheet">

  <section class="card card-front" aria-label="Card front">
    <div class="brand-lockup">
      <span class="brand-mark"></span>
      <span class="brand-name">Brenlo First Aid Training</span>
    </div>
  </section>

  <section class="card card-back" aria-label="Card back">
    <div class="back-brand">
      <span class="brand-mark"></span>
      <span class="brand-name">Brenlo First Aid Training</span>
    </div>
    <div class="divider"></div>
    <div class="contact">
      <p class="person-name">Tobin Marsh</p>
      <p class="contact-row phone">
        <svg class="contact-icon" viewBox="0 0 24 24" aria-hidden="true">
          <path d="M6.5 3h3l1.5 4.5-2 1.5a11 11 0 0 0 6 6l1.5-2 4.5 1.5v3a2 2 0 0 1-2 2A17 17 0 0 1 4.5 5a2 2 0 0 1 2-2z" fill="var(--brand-red)"/>
        </svg>
        0498563027
      </p>
      <p class="contact-row">
        <svg class="contact-icon" viewBox="0 0 24 24" aria-hidden="true">
          <circle cx="12" cy="12" r="11" fill="var(--brand-red)"/>
          <rect x="6" y="8" width="12" height="8" fill="none" stroke="#fff" stroke-width="1.5"/>
          <path d="M6 8l6 5 6-5" fill="none" stroke="#fff" stroke-width="1.5"/>
        </svg>
        tobinmarsh4@mailvex-example.com.au
      </p>
      <p class="contact-row">
        <svg class="contact-icon" viewBox="0 0 24 24" aria-hidden="true">
          <circle cx="12" cy="12" r="11" fill="var(--brand-red)"/>
          <circle cx="12" cy="12" r="6.5" fill="none" stroke="#fff" stroke-width="1.4"/>
          <ellipse cx="12" cy="12" rx="2.8" ry="6.5" fill="none" stroke="#fff" stroke-width="1.2"/>
          <path d="M5.5 12h13" stroke="#fff" stroke-width="1.2"/>
        </svg>
        www.brenlo-example.com.au
      </p>
    </div>
  </section>

</main>
</body>
</html>
```